Exhibition Stand Design for innovative Social Business

We are an innovative social business empowering people to value nature through ZUN, a complementary digital currency. We have attached the TEK_ZUN branding document, and are needing a design for our exhibition stand (https://fairbuildlab.com/produit/stand-parapluie-classic-pvc-3x4c/. The attached doc mocks up a stand on page 32, though we would like some messaging included, in line with our website www.tekzun.ch. You will see there how the branding concept has been implemented with the TEK:GROW, SHARE, THRIVE wording, as well as all of us gain. Our green colours are included in the branding document. Many thanks!

Industry/Entity Type

Environment

Font styles to use
Other font styles liked:
• As per our attached fonts

Requirements
Must have
• Our attached branding guidelines gives our look and feel - Innovative / Dynamic / Vibrant / Reliable / Accessible / Connected.

```html
<!DOCTYPE html>
<html lang="en">
<head>
<meta charset="utf-8">
<title>TEKZUN exhibition stand</title>
<link href="https://fonts.googleapis.com/css2?family=Lexend:wght@500;700&display=swap" rel="stylesheet">
<style>
  :root {
    --mint: #4fe6b8;
    --mint-deep: #3fe68f;
    --lime: #22ee3a;
    --lime-dark: #1fae35;
    --ink: #0b0b0b;
    --white: #ffffff;
    --bg: #f2f2f2;
    --photo-dark: #3a2a1f;
    --photo-warm: #b9804a;
    --photo-sun: #f1b521;
  }
  * { box-sizing: border-box; margin: 0; padding: 0; }
  html, body { width: 1200px; height: 908px; overflow: hidden; background: var(--bg); }
  body { position: relative; font-family: "Lexend", sans-serif; }

  .backwall {
    position: absolute; left: 60px; top: 100px;
    width: 860px; height: 700px;
    display: flex; overflow: hidden;
  }
  .panel { position: relative; height: 100%; overflow: hidden; }

  .panel--brand {
    width: 340px;
    background: linear-gradient(90deg, var(--mint) 0%, var(--mint-deep) 100%);
  }
  .brand-lockup {
    position: absolute; top: 170px; left: 0; width: 100%;
    text-align: center; color: var(--ink);
  }
  .brand-name { font-weight: 700; font-size: 58px; letter-spacing: -1px; line-height: 1; }
  .brand-tagline { font-weight: 500; font-size: 22px; margin-top: 10px; }
  .brand-circle {
    position: absolute; left: -10px; bottom: -30px;
    width: 230px; height: 260px; border-radius: 50%;
    background: linear-gradient(135deg, #6ff0d4 0%, #eafcf6 100%);
  }
  .brand-url {
    position: absolute; left: 90px; bottom: 60px;
    font-size: 11px; font-weight: 500; color: var(--ink);
    transform: rotate(-12deg);
  }

  .panel--photo {
    width: 350px;
    background:
      radial-gradient(ellipse 55% 45% at 78% 72%, var(--photo-sun) 0%, rgba(241,181,33,0) 100%),
      radial-gradient(ellipse 45% 40% at 62% 35%, #e0b98a 0%, rgba(224,185,138,0) 100%),
      linear-gradient(180deg, var(--photo-dark) 0%, var(--photo-warm) 55%, #2a2230 100%);
  }
  .message-box {
    position: absolute; left: 20px; top: 120px;
    padding: 14px 16px 12px;
    background: rgba(60, 40, 30, 0.72); border-radius: 8px;
    color: var(--white); font-weight: 500; font-size: 27px; line-height: 1.2;
  }
  .message-box .lead { color: var(--mint-deep); }

  .panel--accent { flex: 1; background: var(--lime); }
  .accent-circle {
    position: absolute; right: -30px; top: -40px;
    width: 170px; height: 210px; border-radius: 50%;
    background: linear-gradient(90deg, #ffffff 0%, #8df08f 100%);
  }

  .counter {
    position: absolute; left: 950px; top: 560px;
    width: 200px; height: 240px;
    background: linear-gradient(90deg, var(--mint-deep) 0%, var(--lime) 60%, var(--lime-dark) 100%);
    border-top: 6px solid var(--ink); border-bottom: 6px solid var(--ink);
    display: flex; align-items: center; justify-content: center;
  }
  .counter-slogan {
    font-weight: 700;
    font-size: 28px; line-height: 1.15; color: var(--white); text-align: center;
  }
</style>
</head>
<body>
  <section class="backwall">
    <div class="panel panel--brand">
      <div class="brand-lockup">
        <div class="brand-name">TEKZUN</div>
        <div class="brand-tagline">all of us gain</div>
      </div>
      <div class="brand-circle"></div>
      <div class="brand-url">www.tekzun.ch</div>
    </div>
    <div class="panel panel--photo" role="img" aria-label="Photo of a smiling woman holding a bunch of sunflowers">
      <div class="message-box">
        <div class="lead">TEK:</div>
        <div>GROW</div>
        <div>SHARE</div>
        <div>THRIVE</div>
      </div>
    </div>
    <div class="panel panel--accent">
      <div class="accent-circle"></div>
    </div>
  </section>
  <aside class="counter">
    <div class="counter-slogan">all of us<br>gain</div>
  </aside>
</body>
</html>
```